Reservation Confirmation Template

Update:

- added more clarification about what content needs to be included.
- changed project to guaranteed status
- Added $50 to first place

We are a vacation rental company in need of an email template to be used for reservation confirmations. This will be turned into HTML which will be uploaded to our property management system which will use merge fields to populate the actual content. for the purposes of this project, you can use dummy text.

It should be branded and include a section thanking the guest for booking, reservation details, property details, policy details, checkin instructions, etc.

I tried to include a screenshot of our website but it won't allow me to upload it because the dimensions are too large. Please check out our website to use as guidance for look and feel. https://restwillow.net

There should be a place holder for a property image. There should also be a place holder at the bottom for additional services.

Visit our website for branding. I have digital assets such as icons, logos, etc if you require additional branded images or graphics, please message me. I can give you access to our Cloudvault drive.

See the brand guidelines for our colors and fonts.

Target Market(s)

Confirmed vacation rental guests

Industry/Entity Type

Hotel

Font styles to use
Other font styles liked:
• See brand guidelines

Requirements
Must have
• If you think about booking a hotel and receiving a confirmation, that is what we are looking for. The difference for us is that we are a vacation rental company so there are many more details in our confirmations versus a hotel. As such, the following sections need to be included:

Guest Details
- Name
- Phone Number
- Email Address
- # Adults
- # Kids

Property Details
- Image placeholder
- Property Name
- Property Address

- Access Instructions (door code)
- Check in Instructions
- Checkout Instructions
- Parking Details
- Wifi Instructions
- House Rules

Getting Help
- Phone Number
- Email
- Hours
- Emergency Contact

Additional Services
- 3 placeholders split into thirds 100% width at the bottom

In my mind, each section would have a header with either some kind of icon or small graphic. We have already paid to have custom icons created. I will include those in the upload section.
Nice to have
• Everything is mentioned in the project description
Should not have

```html
<!DOCTYPE html>
<html lang="en">
<head>
<meta charset="utf-8">
<title>Rest Willow – Reservation Confirmation</title>
<link rel="stylesheet" href="https://fonts.googleapis.com/css2?family=Montserrat:wght@400;500;600;700;800&family=Crimson+Text:ital@1&display=swap">
<style>
:root{
  --page:#f2f2f2;
  --card:#ffffff;
  --ink:#111111;
  --coral:#f4845f;
  --mint:#a8fcd2;
  --grey-band:#f0f0f0;
  --rule:#dddddd;
  --photo-warm:#c9b9a4;
  --photo-pool:#7fc7cf;
  --photo-room:#d8d6d2;
}
*{box-sizing:border-box;margin:0;padding:0}
html,body{width:1200px;height:3992px;overflow:hidden}
body{background:var(--page);font-family:"Montserrat",sans-serif;color:var(--ink)}
.email{position:absolute;left:242px;top:167px;width:716px;height:3658px;background:var(--card)}
.abs{position:absolute}
.center{left:0;width:100%;text-align:center}
.brand-name{top:48px;font-weight:800;font-size:52px;letter-spacing:1px;line-height:60px}
.brand-tag{top:112px;font-size:18px;font-weight:500;line-height:22px}
.title{top:200px;font-weight:800;font-size:44px;line-height:50px;letter-spacing:-.5px}
.photo{box-shadow:0 4px 12px rgba(0,0,0,.18);border:4px solid #fff}
.hero-photo{left:50px;top:280px;width:620px;height:342px;background:linear-gradient(180deg,#9bc4da 0%,var(--photo-warm) 40%,var(--photo-pool) 62%,#bdb6ac 100%)}
.confirmed{top:668px;color:var(--coral);font-weight:700;font-size:31px;line-height:40px}
.intro,.policy-text{font-family:"Crimson Text",serif;font-style:italic;font-size:18px;line-height:29px;text-align:center;left:46px;width:624px}
.intro{top:718px}
.section-bar{left:47px;width:622px;height:54px;background:var(--mint);text-align:center;font-weight:700;font-size:26px;line-height:54px;letter-spacing:.5px}
.illustration{background:linear-gradient(135deg,#fde3d8,#e3fbee);border-radius:12px}
.row-icon{width:34px;height:34px;border-radius:50%;background:var(--coral);display:flex;align-items:center;justify-content:center}
.row-icon svg{width:20px;height:20px}
.row-text{font-size:22px;font-weight:500;line-height:34px}
.dash{height:0;border-top:1px dashed var(--rule)}
.detail-label{font-size:22px;font-weight:500;line-height:30px}
.detail-value{font-size:22px;font-weight:700;line-height:30px}
.amenity{width:124px;height:124px;border-radius:50%;border:1px dashed var(--rule);display:flex;align-items:center;justify-content:center}
.amenity-label{width:200px;text-align:center;font-weight:700;font-size:24px;line-height:30px}
.property{left:0;top:1869px;width:716px;height:567px;background:var(--mint)}
.property-heading{top:24px;font-weight:700;font-size:26px;line-height:34px}
.room-photo{left:47px;top:83px;width:622px;height:346px;background:linear-gradient(90deg,var(--photo-room) 0%,#ecebe8 40%,#6f7a62 55%,#c4bfb5 100%)}
.property-name{top:461px;font-weight:700;font-size:30px;line-height:38px}
.property-meta{top:510px;font-size:21px;font-weight:500;line-height:26px}
.btn{height:62px;text-align:center;font-weight:700;font-size:29px;line-height:58px;border:2px solid var(--coral)}
.btn-modify{left:93px;top:2489px;width:223px;background:var(--coral);color:#fff}
.btn-cancel{left:399px;top:2489px;width:225px;background:#fff}
.policy{left:0;top:2607px;width:716px;height:429px;background:var(--grey-band)}
.policy-heading{top:28px;font-weight:700;font-size:26px;line-height:34px}
.accent{height:3px;width:62px;background:var(--coral)}
.btn-read{left:246px;top:329px;width:223px;height:60px;border:2px solid var(--coral);text-align:center;font-weight:700;font-size:27px;line-height:56px}
.help-heading{left:53px;top:3090px;font-weight:700;font-size:26px;line-height:32px}
.emergency-frame{left:436px;top:3131px;width:245px;height:228px}
.emergency-label{left:436px;width:245px;text-align:center;top:3278px;font-size:22px;font-weight:500;line-height:28px}
.emergency-number{left:436px;width:245px;text-align:center;top:3312px;font-size:22px;font-weight:700;color:var(--coral);line-height:28px}
.services{left:0;top:3398px;width:716px;height:152px;background:var(--coral);color:#fff}
.services-heading{top:28px;font-weight:700;font-size:28px;line-height:34px}
.services-text{top:93px;font-size:21px;font-weight:500;line-height:26px}
.social{left:0;top:3578px;width:716px;display:flex;justify-content:center;align-items:center;gap:22px}
.social-handle{font-family:"Crimson Text",serif;font-style:italic;font-size:22px;margin-right:6px}
.social-dot{width:36px;height:36px;border-radius:50%;border:3px solid var(--ink)}
</style>
</head>
<body>
<main class="email">
  <header>
    <div class="abs center brand-name">REST WILLOW</div>
    <div class="abs center brand-tag">vacation rentals reinvented.</div>
    <h1 class="abs center title">THANK YOU FOR BOOKING</h1>
  </header>

  <div class="abs photo hero-photo" role="img" aria-label="Property photo: backyard pool with yellow umbrellas and lounge chairs"></div>
  <h2 class="abs center confirmed">Your reservation is confirmed</h2>
  <p class="abs intro">If you think about booking a hotel and receiving a confirmation, that is what we are looking for. The difference for us is that we are a vacation rental company so there are many more details in our confirmations versus a hotel.</p>

  <!-- Guest details -->
  <div class="abs section-bar" style="top:840px">GUEST DETAILS</div>
  <div class="abs illustration" style="left:96px;top:977px;width:136px;height:158px" role="img" aria-label="Line illustration of a traveller with luggage"></div>

  <div class="abs row-icon" style="left:318px;top:938px"><svg viewBox="0 0 20 20" fill="none" stroke="#fff" stroke-width="1.8"><circle cx="10" cy="7" r="3.5"/><path d="M3.5 17c1-3.5 3.5-5 6.5-5s5.5 1.5 6.5 5"/></svg></div>
  <div class="abs row-text" style="left:367px;top:938px">Harlan Pike</div>
  <div class="abs dash" style="left:318px;top:987px;width:352px"></div>

  <div class="abs row-icon" style="left:318px;top:1004px"><svg viewBox="0 0 20 20" fill="none" stroke="#fff" stroke-width="1.8"><path d="M5 3h3l1.5 4-2 1.5a9 9 0 0 0 4 4l1.5-2 4 1.5v3a1.5 1.5 0 0 1-1.5 1.5A13 13 0 0 1 3.5 4.5 1.5 1.5 0 0 1 5 3z"/></svg></div>
  <div class="abs row-text" style="left:367px;top:1004px">555-010-2468</div>
  <div class="abs dash" style="left:318px;top:1054px;width:352px"></div>

  <div class="abs row-icon" style="left:318px;top:1071px"><svg viewBox="0 0 20 20" fill="none" stroke="#fff" stroke-width="1.8"><rect x="3" y="5" width="14" height="10" rx="1"/><path d="M3 5l7 6 7-6"/></svg></div>
  <div class="abs row-text" style="left:367px;top:1071px">harlan@mailbox.net</div>
  <div class="abs dash" style="left:318px;top:1121px;width:352px"></div>

  <div class="abs row-icon" style="left:318px;top:1138px"><svg viewBox="0 0 20 20" fill="none" stroke="#fff" stroke-width="1.8"><circle cx="10" cy="6" r="3"/><path d="M5 17v-4a5 5 0 0 1 10 0v4"/></svg></div>
  <div class="abs row-text" style="left:367px;top:1138px">Adults: 2</div>
  <div class="abs row-icon" style="left:515px;top:1138px"><svg viewBox="0 0 20 20" fill="none" stroke="#fff" stroke-width="1.8"><circle cx="10" cy="10" r="6.5"/><circle cx="8" cy="9" r=".6"/><circle cx="12" cy="9" r=".6"/><path d="M7.5 12.5c1.5 1.2 3.5 1.2 5 0"/></svg></div>
  <div class="abs row-text" style="left:561px;top:1138px">Kids: 1</div>

  <!-- Reservation detail -->
  <div class="abs section-bar" style="top:1235px">RESERVATION DETAIL</div>
  <div class="abs illustration" style="left:102px;top:1387px;width:124px;height:155px" role="img" aria-label="Line illustration of a hand tapping a door keypad on a phone"></div>

  <div class="abs detail-label" style="left:319px;top:1349px">Access (door code):</div>
  <div class="abs detail-value" style="left:319px;top:1380px">01234 567890</div>
  <div class="abs dash" style="left:318px;top:1423px;width:352px"></div>
  <div class="abs detail-label" style="left:319px;top:1433px">Check-in:</div>
  <div class="abs detail-value" style="left:319px;top:1464px">Fri, Dec 25</div>
  <div class="abs dash" style="left:318px;top:1507px;width:352px"></div>
  <div class="abs detail-label" style="left:319px;top:1515px">Checkout:</div>
  <div class="abs detail-value" style="left:319px;top:1546px">Sun, Dec 27</div>

  <div class="abs amenity" style="left:93px;top:1646px"><svg width="76" height="56" viewBox="0 0 76 56" fill="none" stroke="#111" stroke-width="5" stroke-linejoin="round"><path d="M14 24l8-16h32l8 16"/><rect x="6" y="24" width="64" height="20" rx="5" fill="var(--mint)"/><path d="M14 44v8M62 44v8"/><path d="M28 34h20"/></svg></div>
  <div class="abs amenity-label" style="left:55px;top:1789px">Parking</div>

  <div class="abs amenity" style="left:281px;top:1646px"><svg width="80" height="64" viewBox="0 0 80 64" fill="none" stroke="#111" stroke-width="4" stroke-linecap="round"><path d="M6 22a48 48 0 0 1 68 0" stroke="var(--mint)" stroke-width="8"/><path d="M6 22a48 48 0 0 1 68 0"/><path d="M16 32a34 34 0 0 1 48 0"/><path d="M26 42a20 20 0 0 1 28 0"/><circle cx="40" cy="54" r="5"/></svg></div>
  <div class="abs amenity-label" style="left:243px;top:1789px">Wifi</div>

  <div class="abs amenity" style="left:483px;top:1646px"><svg width="84" height="64" viewBox="0 0 84 64" fill="none" stroke="#111" stroke-width="3"><rect x="12" y="6" width="60" height="24" fill="var(--mint)"/><rect x="20" y="14" width="18" height="10" rx="3" fill="#fff"/><rect x="46" y="14" width="18" height="10" rx="3" fill="#fff"/><rect x="6" y="30" width="72" height="20"/><path d="M8 50v10M76 50v10M6 38h72"/></svg></div>
  <div class="abs amenity-label" style="left:445px;top:1789px">House Rules</div>

  <!-- Property details -->
  <section class="abs property">
    <h2 class="abs center property-heading">PROPERTY DETAILS</h2>
    <div class="abs photo room-photo" role="img" aria-label="Property photo: bedroom with white bed and tropical leaf wallpaper"></div>
    <div class="abs center property-name">Harbor Crest Lofts 5</div>
    <div class="abs center property-meta">4 BR / 4 BA / 12 PPL - Nashville, TN</div>
  </section>

  <div class="abs btn btn-modify">MODIFY</div>
  <div class="abs btn btn-cancel">CANCEL</div>

  <!-- Policy -->
  <section class="abs policy">
    <h2 class="abs center policy-heading">POLICY DETAILS</h2>
    <div class="abs accent" style="left:327px;top:66px"></div>
    <p class="abs policy-text" style="top:92px">This Privacy Policy describes Our policies and procedures on the collection, use and disclosure of Your information when You use the Service and tells You about Your privacy rights and how the law protects You.</p>
    <p class="abs policy-text" style="top:207px">We use Your Personal data to provide and improve the Service. By using the Service, You agree to the collection and use of information in accordance with this Privacy Policy.</p>
    <div class="abs btn-read">READ MORE</div>
  </section>

  <!-- Getting help -->
  <h2 class="abs help-heading">GETTING HELP</h2>
  <div class="abs accent" style="left:53px;top:3130px"></div>

  <div class="abs row-icon" style="left:51px;top:3160px"><svg viewBox="0 0 20 20" fill="none" stroke="#fff" stroke-width="1.8"><path d="M5 3h3l1.5 4-2 1.5a9 9 0 0 0 4 4l1.5-2 4 1.5v3a1.5 1.5 0 0 1-1.5 1.5A13 13 0 0 1 3.5 4.5 1.5 1.5 0 0 1 5 3z"/></svg></div>
  <div class="abs row-text" style="left:99px;top:3160px">555-010-2468</div>
  <div class="abs dash" style="left:51px;top:3212px;width:350px"></div>
  <div class="abs row-icon" style="left:51px;top:3227px"><svg viewBox="0 0 20 20" fill="none" stroke="#fff" stroke-width="1.8"><rect x="3" y="5" width="14" height="10" rx="1"/><path d="M3 5l7 6 7-6"/></svg></div>
  <div class="abs row-text" style="left:99px;top:3227px">harlan@mailbox.net</div>
  <div class="abs dash" style="left:51px;top:3278px;width:350px"></div>
  <div class="abs row-icon" style="left:51px;top:3293px"><svg viewBox="0 0 20 20" fill="none" stroke="#fff" stroke-width="1.8"><circle cx="10" cy="10" r="6.5"/><path d="M10 6.5V10l2.5 1.5"/></svg></div>
  <div class="abs row-text" style="left:99px;top:3293px">10am to 8pm</div>

  <svg class="abs emergency-frame" viewBox="0 0 245 228" fill="none" stroke="var(--mint)" stroke-width="2"><path d="M1 60V1h60M244 168v59h-60"/></svg>
  <div class="abs illustration" style="left:487px;top:3146px;width:132px;height:119px" role="img" aria-label="Line illustration of a support agent with headset"></div>
  <div class="abs emergency-label">Emergency Contact</div>
  <div class="abs emergency-number">555-010-2468</div>

  <!-- Additional services -->
  <section class="abs services">
    <h2 class="abs center services-heading">ADDITIONAL SERVICES</h2>
    <div class="abs accent" style="left:327px;top:74px;background:#fff"></div>
    <p class="abs center services-text">3 placeholders split into thirds 100% width at the bottom</p>
  </section>

  <footer class="abs social">
    <span class="social-handle">@restwillowco</span>
    <span class="social-dot"></span>
    <span class="social-dot"></span>
    <span class="social-dot"></span>
  </footer>
</main>
</body>
</html>
```